Brightmere Holdings - Business Cards

We would need to design our Company Business Cards for the following People:

1. Thomas Pirelli
Director/Licensee-In-Charge
M: 0412 579 304
T: (02) 7314 2296
E: thomas@brightmere.com.au
Website: www.brightmereholdings.com

2. Marcus Holt
Project Manager
M: 0421 367 915
T: (02) 7314 2296
E: marcus@brightmereholdings.com

3. Priya Ravindrasekar
Property Officer
M: 0477 218 643
T: (02) 7314 2296
E: priya@brightmereholdings.com

Address: Level 9, 27 Harbour Lane W, Parramatta NSW 2150
The above address is the SAME for ALL Cards.

This Card is to be Double-Sided.
Front - With the above Information & Details.
Back - Showing the Services:
Property Services, Financial Solutions, Special Projects.

ALL Office Locations:
Sydney: (02) 7314 2296
Melbourne: (03) 9241 5503
Brisbane: (07) 3466 1982
Malaysia (JB): (+601) 7293 6048
Singapore: (+65) 9182 4637

We intend on making a Design/Template for the Business Card & duplicating these Business Cards for the above 3x People.
Please USE & REFER to the above FULL Name, Job Title, Mobile, Office Phone, Email & Website.

```html
<!DOCTYPE html>
<html lang="en">
<head>
<meta charset="utf-8">
<title>Brightmere Holdings – Business Cards</title>
<link href="https://fonts.googleapis.com/css2?family=Lato:wght@400;700;900&display=swap" rel="stylesheet">
<style>
  :root {
    --page-bg: #f2f2f2;
    --card-dark: #333333;
    --card-light: #f7f7f7;
    --ink: #1a1a1a;
    --ink-soft: #333333;
    --lime: #c9d300;
    --white: #ffffff;
    --band-dark: #2e2e2e;
  }
  * { margin: 0; padding: 0; box-sizing: border-box; }
  html, body {
    width: 1200px;
    height: 757px;
    overflow: hidden;
    background: var(--page-bg);
    font-family: "Lato", Arial, sans-serif;
  }
  .canvas {
    position: relative;
    width: 1200px;
    height: 757px;
  }
  .card {
    position: absolute;
    top: 195px;
    width: 499px;
    height: 299px;
    overflow: hidden;
  }

  /* Back of card */
  .card--back {
    left: 85px;
    background: var(--card-dark);
    color: var(--white);
    text-align: center;
  }
  .brand {
    font-weight: 700;
    letter-spacing: 0.2em;
    text-transform: uppercase;
    white-space: nowrap;
  }
  .card--back .brand {
    position: absolute;
    top: 78px;
    left: 0;
    width: 100%;
    font-size: 17px;
    color: var(--white);
  }
  .services {
    position: absolute;
    top: 158px;
    left: 0;
    width: 100%;
    font-size: 13.5px;
    font-weight: 900;
    text-transform: uppercase;
    letter-spacing: 0.01em;
  }
  .services .dot {
    color: var(--lime);
    margin: 0 8px;
  }
  .offices {
    position: absolute;
    top: 228px;
    left: 0;
    width: 100%;
    font-size: 11px;
    line-height: 17px;
  }
  .offices__title {
    color: var(--lime);
    font-weight: 700;
    text-decoration: underline;
    margin-bottom: 1px;
  }
  .offices .sep {
    color: var(--lime);
    margin: 0 5px;
  }

  /* Front of card */
  .card--front {
    left: 650px;
    background: var(--card-light);
    color: var(--ink);
  }
  .card--front .brand {
    position: absolute;
    top: 48px;
    right: 35px;
    font-size: 15px;
    color: var(--ink);
    display: flex;
    align-items: center;
    gap: 8px;
  }
  .brand__mark {
    width: 8px;
    height: 8px;
    background: var(--lime);
  }
  .person {
    position: absolute;
    top: 84px;
    left: 29px;
  }
  .person__name {
    font-size: 13.5px;
    font-weight: 700;
    text-transform: uppercase;
  }
  .person__name .surname { color: var(--lime); }
  .person__role {
    font-size: 10px;
    color: var(--ink-soft);
    margin-top: 2px;
  }
  .address {
    position: absolute;
    top: 140px;
    left: 29px;
    font-size: 11px;
    font-weight: 700;
    color: var(--lime);
    line-height: 15px;
  }
  .contact {
    position: absolute;
    top: 191px;
    left: 29px;
    list-style: none;
    font-size: 10.5px;
    color: var(--ink);
  }
  .contact li {
    display: flex;
    align-items: center;
    height: 18.5px;
  }
  .contact svg {
    width: 10px;
    height: 10px;
    margin-right: 11px;
    fill: var(--lime);
  }
  .website {
    position: absolute;
    top: 245px;
    left: 29px;
    font-size: 11px;
    font-weight: 900;
    letter-spacing: 0.04em;
    color: var(--lime);
  }
  .footer-band {
    position: absolute;
    left: 0;
    bottom: 0;
    width: 499px;
    height: 12px;
  }
</style>
</head>
<body>
<main class="canvas">

  <section class="card card--back" aria-label="Business card back">
    <div class="brand">Brightmere Holdings</div>
    <p class="services">
      Property Services<span class="dot">•</span>Financial Solutions<span class="dot">•</span>Special Projects.
    </p>
    <div class="offices">
      <p class="offices__title">All Office Locations:</p>
      <p>Sydney: (02) 7314 2296<span class="sep">|</span>Melbourne: (03) 9241 5503</p>
      <p>Brisbane: (07) 3466 1982<span class="sep">|</span>Malaysia (JB): (+601) 7293 6048<span class="sep">|</span>Singapore: (+65) 9182 4637</p>
    </div>
  </section>

  <section class="card card--front" aria-label="Business card front">
    <div class="brand"><span class="brand__mark"></span>Brightmere Holdings</div>

    <div class="person">
      <p class="person__name">Thomas <span class="surname">Ashcombe</span></p>
      <p class="person__role">Director/Licensee-In-Charge</p>
    </div>

    <p class="address">Level 9, 27 Harbour Lane W,<br>Parramatta NSW 2150</p>

    <ul class="contact">
      <li>
        <svg viewBox="0 0 10 10" aria-hidden="true"><path d="M2.5 0h5a1 1 0 0 1 1 1v8a1 1 0 0 1-1 1h-5a1 1 0 0 1-1-1V1a1 1 0 0 1 1-1zm0.6 1.2v6.6h3.8V1.2zM5 8.3a0.5 0.5 0 1 0 0 1 0.5 0.5 0 0 0 0-1z"/></svg>
        0412 579 304
      </li>
      <li>
        <svg viewBox="0 0 10 10" aria-hidden="true"><path d="M0 3c1-2 9-2 10 0v1.3H7.3V3H2.7v1.3H0zM2 5h6l1.5 4h-9zM5 5.8a1.3 1.3 0 1 0 0 2.6 1.3 1.3 0 0 0 0-2.6z"/></svg>
        (02) 7314 2296
      </li>
      <li>
        <svg viewBox="0 0 10 10" aria-hidden="true"><path d="M0 2h10v0.8L5 6 0 2.8zM0 3.9l5 3.2 5-3.2V8H0z"/></svg>
        thomas@brightmere.com.au
      </li>
    </ul>

    <p class="website">www.brightmereholdings.com</p>

    <svg class="footer-band" viewBox="0 0 499 12" preserveAspectRatio="none" aria-hidden="true">
      <rect x="0" y="2" width="499" height="10" fill="var(--band-dark)"/>
      <polygon points="288,0 462,0 456,12 284,12" fill="var(--white)"/>
      <polygon points="291,1 459,1 454,12 287,12" fill="var(--lime)"/>
    </svg>
  </section>

</main>
</body>
</html>
```